Circus Poster 2016

We want to revise our circus poster for our 2016 tour. We very much liked the poster we used last year (attached) and want to stay with this colour scheme and with this logo. However, we want to enhance the family friendliness of the poster, so perhaps the addition of a family having a great time would be a good idea.

The winner will be paid to modify this poster for each of the 30 events we are doing this year plus making a flyer (based on the poster design). So the winner of this contest gets a job for a year.

Circus

```html
<!DOCTYPE html>
<html lang="en">
<head>
<meta charset="utf-8">
<title>Marlow's Circus – Aylesbury</title>
<link rel="stylesheet" href="https://fonts.googleapis.com/css2?family=Oswald:wght@500;600&display=swap">
<style>
  :root {
    --ink-dark: #160d12;
    --glow-red: #7a1426;
    --glow-purple: #3b1a4d;
    --glow-gold: #6b4a12;
    --circus-red: #e0393f;
    --teal: #2fb7ad;
    --cream: #f4e9c8;
    --tent-red: #c9303a;
    --sun-gold: #c98a2a;
    --white: #ffffff;
  }
  * { margin: 0; padding: 0; box-sizing: border-box; }
  html, body { width: 778px; height: 1200px; overflow: hidden; background: var(--ink-dark); }
  .poster {
    position: relative;
    width: 778px;
    height: 1200px;
    overflow: hidden;
    font-family: "Oswald", "Arial Narrow", sans-serif;
    color: var(--white);
    background:
      radial-gradient(circle at 12% 88%, var(--glow-gold) 0, transparent 40%),
      radial-gradient(circle at 90% 15%, var(--glow-purple) 0, transparent 45%),
      radial-gradient(circle at 85% 80%, var(--glow-red) 0, transparent 42%),
      radial-gradient(circle at 15% 20%, var(--glow-red) 0, transparent 40%),
      var(--ink-dark);
  }
  .brand {
    position: absolute;
    top: 16px;
    left: 0;
    width: 100%;
    text-align: center;
    color: var(--circus-red);
    font-weight: 600;
    line-height: 1;
  }
  .brand-name { display: block; font-size: 54px; letter-spacing: 1px; }
  .brand-word { display: block; font-size: 118px; letter-spacing: 6px; margin-top: 10px; }
  .big-top {
    position: absolute;
    left: 89px;
    top: 226px;
    width: 600px;
    height: 600px;
    border-radius: 50%;
    background:
      radial-gradient(circle at 50% 55%, var(--cream) 0, var(--sun-gold) 30%, transparent 62%),
      linear-gradient(180deg, var(--sun-gold) 0%, var(--tent-red) 45%, var(--teal) 80%, var(--tent-red) 100%);
  }
  .venue {
    position: absolute;
    left: 0;
    width: 100%;
    text-align: center;
    font-weight: 600;
    line-height: 1;
    text-transform: uppercase;
  }
  .venue-town { top: 808px; font-size: 96px; letter-spacing: 2px; }
  .venue-park { top: 918px; font-size: 64px; letter-spacing: 1px; }
  .rule { position: absolute; left: 44px; width: 690px; height: 3px; background: var(--teal); }
  .rule-1 { top: 910px; }
  .rule-2 { top: 992px; }
  .rule-3 { top: 1070px; }
  .rule-4 { top: 1150px; }
  .divider { position: absolute; left: 449px; top: 992px; width: 3px; height: 161px; background: var(--teal); }
  .details {
    position: absolute;
    top: 995px;
    height: 155px;
    font-size: 54px;
    font-weight: 500;
    line-height: 1;
    text-transform: uppercase;
    text-align: center;
  }
  .details-address { left: 44px; width: 405px; }
  .details-dates { left: 452px; width: 282px; }
  .details .row { position: absolute; left: 0; width: 100%; }
  .details .row-1 { top: 6px; }
  .details .row-2 { top: 86px; }
  .contact {
    position: absolute;
    top: 1160px;
    left: 0;
    width: 100%;
    text-align: center;
    font-size: 26px;
    font-weight: 500;
    letter-spacing: 1.5px;
    line-height: 1.2;
    text-transform: uppercase;
  }
  .contact .sep { margin: 0 14px; color: var(--teal); }
</style>
</head>
<body>
  <main class="poster">
    <h1 class="brand">
      <span class="brand-name">Marlow's</span>
      <span class="brand-word">CIRCUS</span>
    </h1>

    <div class="big-top" role="img" aria-label="Illustration of a red and teal striped circus big top against a golden sunburst, with an elephant balancing on a ball in the spotlit entrance"></div>

    <p class="venue venue-town">Aylesbury</p>
    <div class="rule rule-1"></div>
    <p class="venue venue-park">Linden Park</p>
    <div class="rule rule-2"></div>

    <div class="details details-address">
      <span class="row row-1">Hartwell</span>
      <span class="row row-2">Road, HP21 4QX</span>
    </div>
    <div class="details details-dates">
      <span class="row row-1">9-12 July</span>
      <span class="row row-2">2015</span>
    </div>
    <div class="divider"></div>
    <div class="rule rule-3"></div>
    <div class="rule rule-4"></div>

    <p class="contact">www.marlowscircus.com<span class="sep">|</span>01632 555 250</p>
  </main>
</body>
</html>
```